" Um grupo de investidores brasileiros e portugueses foi formado para lançar um condomínio em Portugal, nos arredores de Lisboa. A construtora, Zeva! Módulos, é especializada em casas feitas com containers. Vejam nosso instagram @rimo.brisal para conhecer mais sobre o nosso mercado. Apesar das casas serem container, neste projeto elas serão revestidas externamente, será um condomínio de luxo, porém com estilo mais moderno. "

```html
<!DOCTYPE html>
<html lang="pt">
<head>
<meta charset="utf-8">
<title>Verdale – Papelaria</title>
<link rel="stylesheet" href="https://fonts.googleapis.com/css2?family=Montserrat:wght@400;600&display=swap">
<style>
  :root{
    --bg:#2e2e2e;
    --green:#3aa52c;
    --green-light:#5cc23a;
    --green-dark:#2a8a22;
    --paper:#ffffff;
    --paper-shade:#eef0ee;
    --grey-text:#7a7a7a;
    --ghost:#d9dcd9;
  }
  *{margin:0;padding:0;box-sizing:border-box}
  html,body{width:1200px;height:1200px;overflow:hidden;background:var(--bg)}
  body{position:relative;font-family:"Montserrat",Arial,sans-serif}

  .envelope{
    position:absolute;left:72px;top:192px;width:492px;height:900px;
    background:linear-gradient(135deg,var(--paper) 55%,var(--paper-shade));
    overflow:hidden;
  }
  .envelope__flap{position:absolute;left:0;top:0;width:100%;height:90px}
  .envelope__flap-mark{
    position:absolute;left:50%;top:18px;width:34px;height:34px;margin-left:-17px;
    border:2px solid var(--paper);border-radius:50%;
  }
  .envelope__ghost{
    position:absolute;right:-90px;top:360px;width:430px;height:430px;
    border-radius:50%;border:10px solid var(--ghost);opacity:.7;
  }
  .contacts{position:absolute;left:24px;bottom:34px;list-style:none}
  .contacts li{
    display:flex;align-items:center;gap:7px;
    font-size:8px;line-height:15px;color:var(--grey-text);
  }
  .contacts svg{width:9px;height:9px;fill:var(--green)}
  .envelope__brand{
    position:absolute;right:24px;bottom:38px;display:flex;align-items:center;gap:6px;
  }
  .envelope__brand .brand-dot{width:22px;height:22px;border:2px solid var(--green);border-radius:50%}
  .envelope__brand .brand-name{font-size:18px;font-weight:400;color:var(--green);letter-spacing:1px}
  .envelope__brand .brand-sub{font-size:6px;color:var(--green);letter-spacing:1.5px;margin-top:1px}
  .envelope__rule{
    position:absolute;left:24px;right:24px;bottom:22px;height:4px;background:var(--green);
  }

  .folder{
    position:absolute;left:612px;top:192px;width:516px;height:900px;
    background:radial-gradient(circle at 50% 40%,var(--green-light),var(--green) 55%,var(--green-dark));
    overflow:hidden;
  }
  .folder__ghost{
    position:absolute;right:-70px;top:520px;width:320px;height:320px;
    border-radius:50%;border:10px solid rgba(255,255,255,.12);
  }
  .folder__brand{
    position:absolute;left:0;right:0;top:395px;display:flex;justify-content:center;align-items:center;gap:12px;
  }
  .folder__brand .brand-dot{width:52px;height:52px;border:3px solid var(--paper);border-radius:50%}
  .folder__brand .brand-name{font-size:42px;font-weight:400;color:var(--paper);letter-spacing:2px;line-height:1}
  .folder__brand .brand-sub{font-size:9px;color:var(--paper);letter-spacing:4px;margin-top:4px}
</style>
</head>
<body>
  <section class="envelope" aria-label="Envelope Verdale">
    <svg class="envelope__flap" viewBox="0 0 492 90" preserveAspectRatio="none" aria-hidden="true">
      <defs>
        <linearGradient id="flapFill" x1="0" y1="0" x2="1" y2="0">
          <stop offset="0" stop-color="#2f9a25"/>
          <stop offset=".5" stop-color="#4fbb33"/>
          <stop offset="1" stop-color="#2f9a25"/>
        </linearGradient>
      </defs>
      <path d="M0 0H492V62Q492 72 470 72H22Q0 72 0 62Z" fill="url(#flapFill)"/>
    </svg>
    <div class="envelope__flap-mark"></div>
    <div class="envelope__ghost"></div>

    <ul class="contacts">
      <li><svg viewBox="0 0 10 10"><rect width="10" height="10"/></svg>Zeva! Módulos</li>
      <li><svg viewBox="0 0 10 10"><path d="M5 0a3.5 3.5 0 0 1 3.5 3.5C8.5 6 5 10 5 10S1.5 6 1.5 3.5A3.5 3.5 0 0 1 5 0z"/></svg>Rua das Oliveiras, 12 – Sintra</li>
      <li><svg viewBox="0 0 10 10"><path d="M2 0l2 2.5-1 1.5a6 6 0 0 0 3 3l1.5-1L10 8 8.5 10C4 10 0 6 0 1.5z"/></svg>+351 210 000 000</li>
      <li><svg viewBox="0 0 10 10"><path d="M0 2h10v6H0zM0 2l5 3.5L10 2" stroke="#fff" stroke-width=".8"/></svg>@rimo.brisal · ola@verdale.pt</li>
    </ul>

    <div class="envelope__brand">
      <span class="brand-dot"></span>
      <div>
        <div class="brand-name">VERDALE</div>
        <div class="brand-sub">CASAS CONTAINER</div>
      </div>
    </div>
    <div class="envelope__rule"></div>
  </section>

  <section class="folder" aria-label="Pasta Verdale">
    <div class="folder__ghost"></div>
    <div class="folder__brand">
      <span class="brand-dot"></span>
      <div>
        <div class="brand-name">VERDALE</div>
        <div class="brand-sub">CASAS CONTAINER</div>
      </div>
    </div>
  </section>
</body>
</html>
```